Outdoor Billboard on PVC (double sides)

Hello, i need special design for billboard which is located 15 meters away from the main road. Measures form Billboard: 8 meters X 2 meters. I need Billboard for Window tinting. I have one picture (white Brevanti) which you can use as a main BIG Picture- or you have better idea i am so open to your suggestions. Billboard has to be shocking ... i want to make it look like this is similiar way from style. I have a lot of pictures from my cars which i have done in my garage which we can use it. I dont know if you can use this ... quality? On the billboard so it blames be turn left in 30Meter. My logo wants bi attached- please use it on black background. text which schould be down on the Billboard: Proffesionale Tint my logo VELUNAR put somewhere where looks cool Phone: 0681 2495 307 E-mail: marlow.velunar@kestramail.com Website: www. velunar-glasdunkel.at

Target Market(s)

This billboard wants to be on the border between two countrys..i have my garage company here on the border- where ia am making window. A lot of cars are driving each day nearby so I want that people see this and so they look at where they have left to my garage.

Colors

Designer to choose colors to be used in the design.

Requirements
Must have
• Billboard schould have a BiG picture from white Brevanti with my logo on the side and text Proffesional scarf tint. Down on the board it schould be info Tel, email, website. This measures 8x2 meters

```html
<!DOCTYPE html>
<html lang="de">
<head>
<meta charset="utf-8">
<title>VELUNAR – Billboard Scheibentönung</title>
<link rel="stylesheet" href="https://fonts.googleapis.com/css2?family=Anton&family=Jost:ital,wght@0,600;0,700;1,700&display=swap">
<style>
  :root {
    --stage: #595959;
    --black: #050505;
    --red: #e3232c;
    --grey-rim: #8c8c8c;
    --white: #ffffff;
    --silver-light: #e4e4e4;
    --silver-mid: #9a9a9a;
    --silver-dark: #5e5e5e;
  }
  * { margin: 0; padding: 0; box-sizing: border-box; }
  html, body {
    width: 1016px;
    height: 1200px;
    overflow: hidden;
    background: var(--stage);
  }
  .billboard {
    position: absolute;
    left: 28px;
    top: 480px;
    width: 960px;
    height: 239px;
    background: var(--black);
    overflow: hidden;
  }
  .billboard-shapes {
    position: absolute;
    inset: 0;
    width: 960px;
    height: 239px;
  }
  .brand-name {
    position: absolute;
    left: 24px;
    top: 66px;
    font-family: "Jost", sans-serif;
    font-weight: 700;
    font-size: 23px;
    letter-spacing: 0.5px;
    color: var(--red);
    line-height: 1;
  }
  .tagline {
    position: absolute;
    left: 208px;
    top: 54px;
    font-family: "Jost", sans-serif;
    font-style: italic;
    font-weight: 700;
    font-size: 36px;
    line-height: 1;
    color: var(--white);
    letter-spacing: 0.3px;
  }
  .headline {
    position: absolute;
    left: 22px;
    top: 92px;
    font-family: "Anton", sans-serif;
    font-weight: 400;
    font-size: 70px;
    line-height: 1;
    letter-spacing: 3px;
    background: linear-gradient(180deg, var(--silver-light) 0%, var(--silver-mid) 45%, var(--silver-dark) 55%, var(--silver-light) 100%);
    -webkit-background-clip: text;
    background-clip: text;
    color: transparent;
  }
  .contact-phone {
    position: absolute;
    left: 22px;
    top: 182px;
    font-family: "Anton", sans-serif;
    font-size: 40px;
    line-height: 1;
    color: var(--white);
  }
  .contact-divider {
    position: absolute;
    left: 260px;
    top: 181px;
    width: 2px;
    height: 51px;
    background: var(--white);
  }
  .contact-lines {
    position: absolute;
    left: 274px;
    top: 192px;
    font-family: "Jost", sans-serif;
    font-weight: 700;
    font-size: 12.5px;
    line-height: 18px;
    color: var(--white);
    text-transform: uppercase;
    letter-spacing: 0.2px;
  }
</style>
</head>
<body>
  <section class="billboard">
    <svg class="billboard-shapes" viewBox="0 0 960 239" xmlns="http://www.w3.org/2000/svg">
      <defs>
        <linearGradient id="car-photo-tone" x1="0" y1="1" x2="1" y2="0">
          <stop offset="0" stop-color="#3b3632"/>
          <stop offset="0.35" stop-color="#c9cdd1"/>
          <stop offset="0.65" stop-color="#e6e8ea"/>
          <stop offset="1" stop-color="#e9a842"/>
        </linearGradient>
      </defs>
      <rect class="info-band" x="0" y="174" width="640" height="65" fill="var(--red)"/>
      <path class="photo-rim-red" d="M585 0 Q 505 118 565 239 L 960 239 L 960 0 Z" fill="var(--red)"/>
      <path class="photo-rim-grey" d="M596 0 Q 516 118 576 239 L 960 239 L 960 0 Z" fill="var(--grey-rim)"/>
      <path class="hero-photo" role="img" aria-label="Weißer Brevanti Sportwagen mit getönten Scheiben, Frontansicht in warmem Abendlicht" d="M602 0 Q 522 118 582 239 L 960 239 L 960 0 Z" fill="url(#car-photo-tone)"/>
    </svg>

    <span class="brand-name">VELUNAR</span>

    <p class="tagline">PROFFESIONELLE</p>
    <h1 class="headline">SCHEIBENTÖNUNG</h1>

    <p class="contact-phone">0681 2495 307</p>
    <span class="contact-divider"></span>
    <p class="contact-lines">
      marlow.velunar@kestramail.com<br>
      www.velunar-glasdunkel.at
    </p>
  </section>
</body>
</html>
```